Finance Broker helping people meet their personal and business goals

New business card design,
1st look at the old business card so this makes sense.
I DON'T want:
the subtext "For all your Rural and Commercial Finance".
I DON'T want the: "and Management Consultant" words
I DON'T want the old phone: 07 48213957
I DON'T want the fax number: 07 45826031
I DON'T want the email address: tallowcreek@brightlink.com.au
I DON'T want the flower
What I DO want
I DO want the mobile 0451 836 209 (in larger text)
I DO want:
My name: Dennis Harwell-Lowe
I DO want: Australian Credit Licence 529164 (Tallow Creek Pty Ltd)
I DO want: Principal Finance Broker
I DO want new email: dennis@plotnextstep.com.au
I DO want address: PO Box 928, Tully Qld 4854
I DO want the existing logo (PNS on existing card)

Target Market(s)

Business Borrowers, Home Purchasers, and People wanting to finance cars and plant and equipment

Industry/Entity Type

Financial Service

Contact Information for Business Card

See project description

Font styles to use
Serif

Colors

Designer to choose colors to be used in the design.

Requirements
Must have
• See project description
Nice to have
• Black and Yellow colours
Should not have
• See project description

```html
<!DOCTYPE html>
<html lang="en">
<head>
<meta charset="utf-8">
<title>Plot Next Step – Business Card</title>
<link rel="stylesheet" href="https://fonts.googleapis.com/css2?family=Gilda+Display&family=Open+Sans:ital,wght@0,400;1,700&family=Saira:wght@800&display=swap">
<style>
  :root {
    --page: #e4e5e7;
    --ink: #0b0b0b;
    --panel-dark: #111111;
    --panel-mid: #2a2a2a;
    --lime: #d9e25a;
    --lime-light: #eef0a2;
    --lime-deep: #e2e86a;
    --white: #ffffff;
    --rule: #3a3a22;
  }
  * { margin: 0; padding: 0; box-sizing: border-box; }
  html, body { width: 1200px; height: 1200px; overflow: hidden; background: var(--page); }
  .canvas { position: relative; width: 1200px; height: 1200px; }

  .card {
    position: absolute; left: 100px; top: 316px;
    width: 1000px; height: 568px;
    border-radius: 40px; overflow: hidden;
    background: linear-gradient(180deg, var(--lime-light) 360px, var(--lime-deep) 568px);
  }
  .card__dark {
    position: absolute; left: 0; top: 0; width: 100%; height: 355px;
    background: radial-gradient(ellipse at 50% 35%, var(--panel-mid) 0%, var(--panel-dark) 70%);
  }
  .card__divider {
    position: absolute; left: 0; top: 355px; width: 100%; height: 5px;
    background: var(--white);
  }

  .brand { position: absolute; left: 138px; top: 52px; }
  .brand__name {
    font-family: "Gilda Display", serif; font-size: 43px; color: var(--lime);
    line-height: 1; letter-spacing: 0.5px;
  }
  .brand__member {
    font-family: "Open Sans", sans-serif; font-size: 14px; color: #c9c9b8;
    letter-spacing: 1.6px; margin-top: 8px;
  }
  .brand__mark {
    position: absolute; left: 720px; top: 60px;
    width: 96px; height: 96px; border-radius: 50%; background: var(--lime);
  }

  .person { position: absolute; left: 0; top: 162px; width: 100%; text-align: center; }
  .person__name {
    font-family: "Gilda Display", serif; font-size: 46px; color: var(--lime); line-height: 1.1;
  }
  .person__title {
    font-family: "Open Sans", sans-serif; font-size: 23px; color: var(--white);
    letter-spacing: 1px; margin-top: 8px;
  }
  .phone {
    position: absolute; left: 0; top: 258px; width: 100%; text-align: center;
    font-family: "Saira", sans-serif; font-weight: 800; font-size: 100px;
    color: var(--white); line-height: 1; letter-spacing: 1px;
  }

  .licence {
    position: absolute; left: 60px; top: 378px; width: 880px;
    display: flex; align-items: center; gap: 14px;
  }
  .licence__rule { flex: 1; height: 2px; }
  .licence__rule--left { background: linear-gradient(90deg, transparent, var(--rule)); }
  .licence__rule--right { background: linear-gradient(90deg, var(--rule), transparent); }
  .licence__text {
    font-family: "Open Sans", sans-serif; font-style: italic; font-weight: 700;
    font-size: 22px; color: var(--ink); white-space: nowrap;
  }

  .contact {
    position: absolute; left: 0; top: 414px; width: 100%; text-align: center;
    font-family: "Gilda Display", serif; font-size: 39px; color: var(--ink); line-height: 1.35;
  }
</style>
</head>
<body>
<main class="canvas">
  <section class="card">
    <div class="card__dark"></div>
    <div class="card__divider"></div>

    <header class="brand">
      <div class="brand__name">Plot Next Step</div>
      <div class="brand__member">A Member of the Tallow Creek Group</div>
    </header>
    <div class="brand__mark"></div>

    <div class="person">
      <div class="person__name">Dennis Harwell-Lowe</div>
      <div class="person__title">Principal Finance Broker</div>
    </div>
    <div class="phone">0451 836 209</div>

    <div class="licence">
      <span class="licence__rule licence__rule--left"></span>
      <span class="licence__text">Australian Credit Licence 529164</span>
      <span class="licence__rule licence__rule--right"></span>
    </div>

    <address class="contact" style="font-style: normal;">
      <div>dennis@plotnextstep.com.au</div>
      <div>PO Box 928, Tully Qld 4854</div>
    </address>
  </section>
</main>
</body>
</html>
```